Flyer-Design für gesunde Lebensmittel im Laden
Zielgruppe
Mühlenladen; Es werden eine breite Palette an gesunden Lebensmitteln im Laden z.T. selbst produziert und abgepackt.
Produktpalette siehe Anlage
Neu: Unverpackt in Bedienung wie bei Omas Tante-Emma-Laden.
Individuell zusammengestellte Geschenkkörbe.
Gewürz- und Backmischungen aus eigener Herstellung.
Zielgruppe: Ernährungsbewusste Verbraucher von jung bis alt, die viel Spaß am Kochen und Backen haben.
Aufgabenstellung
Format: Größe des Flyers soll als Beilage für Gemeindemitteilungsblätter passen;
besonderer Aspekt auf Unverpackt, Dinkelprodukte, Müsli, Vegan, glutenfrei und Gewürze
regional & natürlich
Rezept (siehe Anlage) soll integriert werden

```html
<!DOCTYPE html>
<html lang="de">
<head>
<meta charset="utf-8">
<title>Kornhof Auer – Flyer</title>
<link href="https://fonts.googleapis.com/css2?family=Roboto+Slab:wght@300;400;700&family=Kalam:wght@400;700&family=Raleway:wght@300;400&display=swap" rel="stylesheet">
<style>
  :root {
    --stage: #dddce2;
    --paper: #f2f0e8;
    --green: #5ca42e;
    --green-dark: #3f8f27;
    --lime: #cbd95a;
    --lime-line: #c9cf4a;
    --ink: #3a3a3a;
    --photo-grain-a: #c8b59a;
    --photo-grain-b: #e6e6ea;
    --photo-flour-a: #f6f4ef;
    --photo-flour-b: #dcd8cf;
  }
  * { box-sizing: border-box; margin: 0; padding: 0; }
  html, body { width: 1200px; height: 857px; overflow: hidden; }
  body {
    background: var(--stage);
    font-family: "Roboto Slab", serif;
    color: var(--green-dark);
    position: relative;
  }
  .flyer {
    position: absolute;
    top: 26px;
    width: 380px;
    height: 805px;
    background: var(--paper);
    box-shadow: 0 6px 18px rgba(0,0,0,.18);
    overflow: hidden;
  }
  .flyer--front { left: 180px; }
  .flyer--back { left: 640px; }
  .frame {
    position: absolute; inset: 10px 10px 64px 10px;
    border: 1.5px solid var(--lime-line);
    pointer-events: none;
  }
  .photo { position: absolute; left: 0; right: 0; top: 0; }
  .photo--grain {
    height: 360px;
    background: linear-gradient(180deg, var(--photo-grain-b) 0%, #d9d8dc 55%, var(--photo-grain-a) 80%, var(--paper) 100%);
  }
  .photo--flour {
    height: 250px;
    background: radial-gradient(ellipse at 30% 45%, #ffffff 0%, var(--photo-flour-a) 35%, var(--photo-flour-b) 75%, var(--paper) 100%);
  }
  .shop-name {
    position: absolute;
    font-family: "Roboto Slab", serif; font-weight: 400;
    color: var(--green-dark);
  }
  .flyer--front .shop-name { left: 0; right: 0; top: 120px; text-align: center; font-size: 34px; }
  .flyer--back .shop-name { right: 26px; top: 30px; font-size: 17px; }

  .badge {
    position: absolute; border-radius: 50%;
    background: var(--lime); border: 2px solid var(--green);
    box-shadow: 0 0 0 3px var(--lime);
    display: flex; flex-direction: column; align-items: center; justify-content: center;
    text-align: center; color: var(--green-dark); transform: rotate(-10deg);
  }
  .badge__title { font-weight: 700; font-size: 20px; line-height: 1; }
  .badge__text { font-family: "Kalam", cursive; font-weight: 700; font-size: 15px; line-height: 1.1; }
  .flyer--front .badge { width: 118px; height: 118px; right: 22px; top: 300px; }
  .flyer--back .badge { width: 104px; height: 104px; right: 28px; top: 120px; }
  .flyer--back .badge__title { font-size: 17px; }
  .flyer--back .badge__text { font-size: 13px; }

  .tagline {
    position: absolute; left: 60px; top: 380px;
    font-size: 11px; color: var(--ink); font-weight: 400;
  }
  .assortment { position: absolute; left: 20px; right: 20px; top: 430px; text-align: center; }
  .assortment__kicker {
    font-family: "Raleway", sans-serif; font-size: 19px; color: var(--green);
    display: inline-block; border-bottom: 1.5px solid var(--lime-line); padding: 0 4px 2px; margin-bottom: 8px;
  }
  .assortment__line { line-height: 1.15; color: var(--green); }
  .slab { font-weight: 700; font-size: 22px; }
  .script { font-family: "Kalam", cursive; font-weight: 700; font-size: 24px; }

  .band {
    position: absolute; left: 0; right: 0; bottom: 64px; height: 44px;
    background: var(--green); color: #fff;
    font-size: 17px; display: flex; align-items: center; justify-content: center; letter-spacing: .5px;
  }
  .footnote {
    position: absolute; left: 0; right: 0; bottom: 18px; text-align: center;
    color: var(--ink); font-size: 17px; font-weight: 300;
  }
  .footnote b { font-weight: 700; font-size: 20px; }
  .footnote .script { font-size: 18px; color: var(--ink); font-weight: 400; }

  .recipe { position: absolute; left: 28px; right: 26px; top: 232px; color: var(--green-dark); }
  .recipe__heading { font-family: "Kalam", cursive; font-weight: 700; font-size: 24px; color: var(--ink); }
  .recipe__ingredients { list-style: none; font-size: 12px; line-height: 1.45; margin: 2px 0 14px 10px; }
  .recipe__steps { list-style: none; font-size: 12px; line-height: 1.5; font-weight: 300; }
  .recipe__steps li { display: flex; gap: 8px; margin-bottom: 12px; }
  .step-no {
    flex: 0 0 20px; height: 20px; border-radius: 50%; background: var(--lime);
    color: var(--green-dark); font-weight: 700; font-size: 12px;
    display: flex; align-items: center; justify-content: center; margin-top: 1px;
  }
</style>
</head>
<body>

<article class="flyer flyer--front">
  <div class="photo photo--grain" role="img" aria-label="Foto: Haferflocken auf hellem Tisch vor weißer Schale"></div>
  <div class="shop-name">Kornhof Auer</div>
  <div class="badge">
    <span class="badge__title">NEU:</span>
    <span class="badge__text">unverpackte<br>Waren</span>
  </div>
  <p class="tagline">glutenfrei. regional. natürlich</p>
  <section class="assortment">
    <div class="assortment__kicker">WIE BEI TANTE-EMMA</div>
    <div class="assortment__line"><span class="slab">Getreide</span> <span class="script">Müsli</span> <span class="slab">Tee</span></div>
    <div class="assortment__line"><span class="slab">gesundes Naschen &amp; Gebäck</span></div>
    <div class="assortment__line"><span class="script">Saaten &amp; Backzutaten</span> <span class="slab">Gewürze</span></div>
    <div class="assortment__line"><span class="script">Essige &amp; Öle</span> <span class="slab">Dinkelprodukte</span></div>
    <div class="assortment__line"><span class="script">Gewürze und mehr</span></div>
  </section>
  <div class="frame"></div>
  <div class="band">Auweg 7 • 84123 Talheim • Tel. 09876-431</div>
  <p class="footnote"><b>mit</b> <span class="script">tollem Rezept</span> auf der Rückseite</p>
</article>

<article class="flyer flyer--back">
  <div class="photo photo--flour" role="img" aria-label="Foto: Gugelhupfform in Mehl mit Messlöffel"></div>
  <div class="shop-name">Kornhof Auer</div>
  <div class="badge">
    <span class="badge__title">Rezept:</span>
    <span class="badge__text">Energie-Mix<br>Kekse</span>
  </div>
  <section class="recipe">
    <h2 class="recipe__heading">Zutaten:</h2>
    <ul class="recipe__ingredients">
      <li>200 g Energie-Mix</li>
      <li>260 g Dinkelmehl Type 630</li>
      <li>150 g heller Rohrzucker</li>
      <li>1 Prise Salz</li>
      <li>300 g kalte Butter</li>
      <li>1 Ei</li>
    </ul>
    <ol class="recipe__steps">
      <li><span class="step-no">1</span><span>Den Energie-Mix im Mixer grob hacken.</span></li>
      <li><span class="step-no">2</span><span>Mehl, Zucker, Salz, Energie-Mix mischen. Die kalte Butter in kleinen Stücken und das Ei zugeben und daraus einen glatten Teig herstellen. Zu einer ca. 3 cm dicken Platte formen und in Klarsichtfolie wickeln. Den Teig über Nacht kaltstellen.</span></li>
      <li><span class="step-no">3</span><span>Die Teigplatte der Länge nach in 3 gleich große Stücke schneiden. Davon dicke Scheiben abschneiden (ca. 1/2 cm dick) und auf ein mit Backpapier ausgelegtes Blech legen. Im heißen Ofen bei 180° C auf der mittleren Schiene 10-15 Min. goldgelb backen. Auf einem Gitter abkühlen lassen.</span></li>
    </ol>
  </section>
  <div class="frame"></div>
  <div class="band">Auweg 7 • 84123 Talheim • Tel. 09876-431</div>
  <p class="footnote"><b>Lasst</b> <span class="script">es euch gut</span> schmecken.</p>
</article>

</body>
</html>
```